New York College Admissions Consulting Company Looking for a One-Page Flyer Design

We are a college admissions consulting company Harwick Admissions Consulting (www.harwickadmissions.example) and we help students apply to universities. We need a 1-page flyer design to hand out at a science competition for high school students. I attach all the information that should be included in the flyer and the logo. Please make a stylistic and professional looking flyer, which will impress these very smart and sophisticated high school students and even more importantly - their parents. Feel free to move the text around the flyer and to change the font as you see fit. Also, please add a stock picture or two, as you see fit. Also, let me know if I have to pay for the stock photos (if I have to get a license to use the photos on the flyer), and where and how much I would need to pay.

Target Market(s)

Smart and sophisticated high school students and even more importantly - their parents.

Industry/Entity Type

College

Requirements
Must have
• Must look sophisticated. This is an expensive service and parents need to know that our image matches our prices.
Should not have
• Wild colors like red.

```html
<!DOCTYPE html>
<html lang="en">
<head>
<meta charset="utf-8">
<title>Harwick Admissions Consulting – Complimentary Live Online Class</title>
<link rel="stylesheet" href="https://fonts.googleapis.com/css2?family=Mulish:ital,wght@0,400;0,600;0,700;0,800;1,700&display=swap">
<style>
  :root {
    --brand-blue: #1a8fd2;
    --brand-blue-deep: #1479b5;
    --ink: #1b1b1b;
    --paper: #ffffff;
    --photo-light: #e9eef2;
    --photo-mid: #b7c3cc;
    --photo-dark: #5a6570;
  }
  * { box-sizing: border-box; margin: 0; padding: 0; }
  html, body { width: 905px; height: 1200px; overflow: hidden; background: var(--paper); }
  body { font-family: "Mulish", "Century Gothic", sans-serif; color: var(--ink); }

  .flyer { position: relative; width: 905px; height: 1200px; }

  .title-band {
    position: absolute; top: 0; left: 0; width: 100%; height: 82px;
    background: var(--brand-blue);
    display: flex; align-items: center; justify-content: center;
  }
  .title-band h1 { color: var(--paper); font-size: 47px; font-weight: 700; letter-spacing: 0.2px; }

  .class-name {
    position: absolute; top: 106px; left: 0; width: 100%; text-align: center;
    color: var(--brand-blue); font-size: 24px; font-weight: 700;
  }

  .learn-heading { position: absolute; top: 158px; left: 12px; font-size: 19px; font-weight: 700; }

  .learn-list { position: absolute; top: 192px; left: 102px; list-style: none; }
  .learn-list li {
    display: flex; align-items: center; height: 39px;
    font-size: 19.5px; font-weight: 700;
  }
  .learn-list svg { width: 20px; height: 20px; margin-right: 33px; flex: none; }

  .plus { position: absolute; top: 310px; left: 0; width: 100%; text-align: center; font-size: 16px; }

  .live-answers {
    position: absolute; top: 346px; left: 289px; width: 320px; height: 50px;
    background: var(--brand-blue); border-radius: 9px;
    display: flex; align-items: center; justify-content: center;
    color: var(--paper); font-size: 20px;
  }

  .facts-heading {
    position: absolute; top: 396px; left: 12px;
    color: var(--brand-blue); font-size: 25px; font-weight: 700;
  }

  .facts-list { position: absolute; top: 458px; left: 0; width: 860px; list-style: none; }
  .facts-list li {
    position: relative; padding-left: 113px; margin-bottom: 16px;
    font-size: 19.5px; line-height: 31px;
  }
  .facts-list li::before {
    content: ""; position: absolute; left: 63px; top: 12px;
    width: 8px; height: 8px; border-radius: 50%; background: var(--ink);
  }
  .facts-list strong { font-weight: 800; }

  .brand {
    position: absolute; top: 778px; left: 0; width: 100%;
    display: flex; align-items: center; justify-content: center; gap: 22px;
  }
  .brand-dot { width: 58px; height: 58px; border-radius: 50%; background: var(--brand-blue); }
  .brand-name { color: var(--brand-blue); font-size: 38px; font-weight: 600; letter-spacing: 1px; }

  .date-band {
    position: absolute; top: 872px; left: 0; width: 100%; height: 56px;
    background: var(--brand-blue);
    display: flex; align-items: center; justify-content: center;
    color: var(--paper); font-size: 20px; font-weight: 700;
  }

  .photo {
    position: absolute; top: 928px; left: 0; width: 100%; height: 183px;
    background: linear-gradient(180deg, var(--photo-light) 0%, var(--photo-mid) 55%, var(--photo-dark) 100%);
  }

  .contact-band {
    position: absolute; top: 1111px; left: 0; width: 100%; height: 89px;
    background: var(--brand-blue);
    display: flex; flex-direction: column; align-items: center; justify-content: center;
    color: var(--paper); font-size: 22px; font-weight: 700; line-height: 30px;
  }
</style>
</head>
<body>
<main class="flyer">
  <header class="title-band"><h1>Complimentary Live Online Class</h1></header>

  <p class="class-name">“The College Personal Statement and Perfecting Your Narrative”</p>

  <h2 class="learn-heading">Learn How To:</h2>
  <ul class="learn-list">
    <li><svg viewBox="0 0 20 20" aria-hidden="true"><path d="M2 11 L7 16 L18 3" fill="none" stroke="#1b1b1b" stroke-width="2.2"/></svg>Avoid the Most Common Mistakes Made in The Personal Statement</li>
    <li><svg viewBox="0 0 20 20" aria-hidden="true"><path d="M2 11 L7 16 L18 3" fill="none" stroke="#1b1b1b" stroke-width="2.2"/></svg>Compose a Memorable Essay</li>
    <li><svg viewBox="0 0 20 20" aria-hidden="true"><path d="M2 11 L7 16 L18 3" fill="none" stroke="#1b1b1b" stroke-width="2.2"/></svg>Craft a Compelling Narrative</li>
  </ul>

  <p class="plus">+</p>
  <p class="live-answers">Live Answers to Live Questions</p>

  <h2 class="facts-heading">Admission Facts and Tips:</h2>
  <ul class="facts-list">
    <li>In the last <strong>9</strong> years, the Average Ivy League College Admission Rate has dropped by 49%.</li>
    <li>Admission Rate in 2005 - <strong>17.1%</strong></li>
    <li>Admission Rate in 2014 - <strong>8.8%</strong></li>
    <li>The Personal Statement and the Supplemental Essays comprise approximately <strong>25%</strong> of the admission criteria.</li>
    <li>Crafting the Perfect Narrative is vital to your college application. It can mean the difference between an acceptance and a rejection.</li>
  </ul>

  <div class="brand">
    <span class="brand-dot" aria-hidden="true"></span>
    <span class="brand-name">Harwick Admissions Consulting</span>
  </div>

  <p class="date-band">Sunday, May 31, 2015 @ 4 pm-5 pm EST</p>

  <div class="photo" role="img" aria-label="Stock photo of blurred students walking through a bright hallway"></div>

  <footer class="contact-band">
    <span>www.harwickadmissions.example</span>
    <span>1.646.555.0142</span>
  </footer>
</main>
</body>
</html>
```